Veterinary hospital brochure design

we need brochure design for our veterinary hospital, something interesting, catchy and unique. Once we get going we need to add few unique services we offer and should be highlighted.Nice colors, and should be very professional looking. Brochure to be tri fold, nice colors highlight our services.
Like shades of blues or green.This is full service veterinary hospital. We do focus and specialize in Canine reproduction.

pet owners

Hospital

Serif
Script

• catchy words
• unique design
• have our unique services included
• good pictures and catchy words etc etc

```html
<!DOCTYPE html>
<html lang="en">
<head>
<meta charset="utf-8">
<title>Cedar Ridge Hospital for Animals – Tri-fold Brochure</title>
<link rel="stylesheet" href="https://fonts.googleapis.com/css2?family=Roboto+Condensed:wght@700&family=Lato:wght@400;700&display=swap">
<style>
  :root {
    --navy: #1b1f8a;
    --green: #94e63a;
    --green-soft: #a6ee4c;
    --paper: #ffffff;
    --ink: #1d1d1d;
    --brand-ink: #222222;
  }
  html, body {
    margin: 0;
    width: 1200px;
    height: 1200px;
    overflow: hidden;
    background: var(--paper);
  }
  .brochure {
    position: absolute;
    left: 73px;
    top: 230px;
    width: 1068px;
    height: 760px;
    background: var(--paper);
    overflow: hidden;
    font-family: "Lato", sans-serif;
    color: var(--ink);
    box-shadow: 0 2px 10px rgba(0,0,0,0.18);
  }
  .art { position: absolute; inset: 0; }
  .fold {
    position: absolute;
    top: 0;
    width: 1px;
    height: 760px;
    background: rgba(0,0,0,0.06);
  }
  .doctor-name {
    position: absolute;
    left: 39px;
    top: 62px;
    margin: 0;
    font-family: "Roboto Condensed", sans-serif;
    font-weight: 700;
    font-size: 31px;
    line-height: 1;
    color: var(--navy);
  }
  .doctor-title {
    position: absolute;
    left: 39px;
    top: 98px;
    margin: 0;
    font-family: "Roboto Condensed", sans-serif;
    font-weight: 700;
    font-size: 25px;
    line-height: 1;
    color: var(--green);
  }
  .bio {
    position: absolute;
    left: 41px;
    top: 149px;
    width: 280px;
    font-size: 11.6px;
    line-height: 14.9px;
    text-align: justify;
  }
  .bio p { margin: 0 0 14.9px; }
  .brand {
    position: absolute;
    display: flex;
    align-items: center;
    gap: 10px;
    font-family: "Lato", sans-serif;
    font-weight: 400;
    color: var(--brand-ink);
    line-height: 1.1;
  }
  .brand-dot {
    flex: none;
    width: 14px;
    height: 14px;
    border-radius: 50%;
    background: var(--brand-ink);
  }
  .brand-name { display: block; }
  .brand--cover { left: 790px; top: 52px; font-size: 22px; }
  .brand--back { left: 440px; top: 594px; font-size: 19px; }
  .contact {
    position: absolute;
    left: 414px;
    top: 651px;
    width: 240px;
    text-align: center;
    font-size: 12px;
    line-height: 15px;
  }
  .contact p { margin: 0; }
  .contact .phone { margin-top: 5px; }
  .contact .web { margin-top: 5px; }
  .welcome {
    position: absolute;
    left: 751px;
    top: 588px;
    color: #fff;
  }
  .welcome-kicker {
    margin: 0;
    font-family: "Roboto Condensed", sans-serif;
    font-weight: 700;
    font-size: 30px;
    line-height: 1;
  }
  .welcome-name {
    margin: 4px 0 0;
    font-family: "Roboto Condensed", sans-serif;
    font-weight: 700;
    font-size: 34px;
    line-height: 1;
    color: var(--navy);
  }
  .welcome-tail {
    margin: 2px 0 0;
    font-family: "Lato", sans-serif;
    font-weight: 400;
    font-size: 54px;
    line-height: 1;
  }
  .welcome-web {
    margin: 6px 0 0;
    font-size: 14px;
  }
</style>
</head>
<body>
<div class="brochure">
  <svg class="art" width="1068" height="760" viewBox="0 0 1068 760" xmlns="http://www.w3.org/2000/svg">
    <defs>
      <linearGradient id="mistDog" x1="0" y1="0" x2="0" y2="1">
        <stop offset="0" stop-color="#e4e4e4"/>
        <stop offset="0.7" stop-color="#efefef"/>
        <stop offset="1" stop-color="#ffffff"/>
      </linearGradient>
      <linearGradient id="petsGroup" x1="0" y1="0" x2="1" y2="0">
        <stop offset="0" stop-color="#c9c3bb"/>
        <stop offset="0.5" stop-color="#b59a7d"/>
        <stop offset="1" stop-color="#7a7470"/>
      </linearGradient>
      <linearGradient id="vetExam" x1="0" y1="0" x2="1" y2="1">
        <stop offset="0" stop-color="#e8eef0"/>
        <stop offset="0.6" stop-color="#e7d7bd"/>
        <stop offset="1" stop-color="#f3f5f6"/>
      </linearGradient>
    </defs>

    <rect role="img" aria-label="Faded photo of a smiling golden retriever" x="361" y="0" width="357" height="600" fill="url(#mistDog)"/>

    <rect x="718" y="300" width="350" height="460" fill="var(--green)"/>

    <path d="M0,586 C220,592 500,545 722,380 L738,398 C520,575 250,640 0,634 Z" fill="var(--green)"/>
    <path d="M361,760 L361,540 C480,520 620,460 722,382 L718,760 Z" fill="#fff"/>
    <path d="M0,634 C250,640 520,575 738,398 L742,420 C520,600 250,650 0,650 Z" fill="#fff"/>
    <path d="M0,574 C220,580 500,532 722,368" fill="none" stroke="var(--navy)" stroke-width="9"/>

    <path d="M657,0 C690,95 850,140 1068,146" fill="none" stroke="var(--green)" stroke-width="22"/>
    <path d="M657,-6 C690,86 850,128 1068,132" fill="none" stroke="var(--navy)" stroke-width="10"/>

    <path role="img" aria-label="Photo of a veterinarian examining a puppy with a stethoscope"
      d="M732,162 C850,174 960,170 1068,170 L1068,560 L960,560 C900,556 870,536 830,512 C740,460 680,390 680,300 C680,230 700,188 732,162 Z"
      fill="url(#vetExam)"/>
    <path d="M730,152 C694,186 672,250 674,310 C680,400 760,470 840,522 C890,552 920,570 960,570 L1068,570"
      fill="none" stroke="var(--green-soft)" stroke-width="24"/>
    <path d="M730,158 C698,190 678,252 680,310 C686,396 762,464 840,514 C890,546 920,562 960,562 L1068,562"
      fill="none" stroke="var(--navy)" stroke-width="9"/>

    <path role="img" aria-label="Photo of dogs and kittens sitting together"
      d="M20,760 L20,640 C40,600 80,560 130,540 C190,520 260,520 300,540 C340,560 360,600 362,640 L362,760 Z"
      fill="url(#petsGroup)" opacity="0.9"/>
    <rect role="img" aria-label="Photo of a small white and tabby kitten" x="362" y="648" width="68" height="112" rx="30" fill="#d9d3cc"/>
  </svg>

  <div class="fold" style="left:361px"></div>
  <div class="fold" style="left:718px"></div>

  <h1 class="doctor-name">ARUN MEHTA</h1>
  <h2 class="doctor-title">(A/K/A DR. ACE), DVM</h2>
  <div class="bio">
    <p>Dr. Mehta was born in India and raised in Connecticut. He received his DVM from Harbor University and did his clinical work at Lakeview State University. His journey began at Cedar Ridge Hospital for Animals in 2003 working alongside Dr. Daniel Hartwell as an associate. He took ownership of the hospital in 2010. Since his leadership, Cedar Ridge has grown to a new height of compassionate care for our patients.</p>
    <p>While he is particularly known for his canine reproduction and surgical expertise, Dr. Mehta performs a broad spectrum of diagnostic testing and soft tissue surgery for his general practice. His extraordinary skills and intuitive powers regarding veterinary medicine and surgery have won him intense loyalty throughout the community. His practice thrives because of the unquestionable confidence and passion with which he treats each and every animal.</p>
  </div>

  <div class="brand brand--cover"><span class="brand-dot"></span><span class="brand-name">Cedar Ridge<br>Hospital for Animals</span></div>

  <div class="brand brand--back"><span class="brand-dot"></span><span class="brand-name">Cedar Ridge<br>Hospital for Animals</span></div>
  <div class="contact">
    <p>240 Cedar Ridge Road</p>
    <p>Millbrook, CT 06999</p>
    <p class="phone">+1 203-555-0147</p>
    <p class="web">www.cedarridgeanimalhospital.com</p>
  </div>

  <div class="welcome">
    <p class="welcome-kicker">WELCOME TO</p>
    <p class="welcome-name">Cedar Ridge Hospital</p>
    <p class="welcome-tail">for Animals!</p>
    <p class="welcome-web">www.cedarridgeanimalhospital.com</p>
  </div>
</div>
</body>
</html>
```